4 x Designs Required

Hi There,
I require 4 x different designs to be made for 4 new brands of mine however they can be quite interchangeable. HR Wispo and Marketing Wispo can be similar just with a difference in colour. The same goes for the Bulletin brands. This means there are ultimately two designs that need perfecting.

There must be a click here CTA on the banner somewhere. :-)

I require the banners in 728x90 format and 960x90 please.

Please use strap lines on the banners such as:
Essential Whitepapers for HR Professionals
Essential Whitepapers for Marketing Professionals
Your No.1 Whitepaper Resource

The brand names:
HR Wispo
Marketing Wispo
HR Gazettor
Marketing Gazettor

Examples attached.

```html
<!DOCTYPE html>
<html lang="en">
<head>
<meta charset="utf-8">
<title>Whitepaper Brand Banners</title>
<link rel="stylesheet" href="https://fonts.googleapis.com/css2?family=Montserrat:wght@500;600;700;800;900&display=swap">
<style>
  :root {
    --ink: #111111;
    --white: #ffffff;
    --stage-grey: #c6c6c6;
    --texture-grey: #b4b4b8;
    --gold: #ebcf00;
    --sun: #ffe400;
    --purple: #432d5a;
    --purple-soft: #7b6396;
    --slate: #4a5068;
    --orange: #f6a12f;
    --orange-light: #ffc63a;
    --coral: #e07350;
    --coral-deep: #b9685a;
    --cocoa: #4a2a22;
    --steel: #3f5a78;
  }
  * { box-sizing: border-box; margin: 0; padding: 0; }
  html, body { width: 848px; height: 1200px; overflow: hidden; background: var(--white); }
  body { font-family: "Montserrat", sans-serif; color: var(--ink); }
  .canvas { position: relative; width: 848px; height: 1200px; overflow: hidden; background: var(--white); }
  .stage { position: absolute; left: 0; top: 0; width: 848px; height: 683px; background: var(--stage-grey); }
  .set-title { position: absolute; left: 0; width: 848px; text-align: center; font-weight: 900; font-size: 25.5px; line-height: 1; }
  .set-title--second { top: 84px; }
  .set-title--first { top: 724px; }

  .banner { position: absolute; left: 0; width: 848px; overflow: hidden; background: var(--white); }
  .banner--slim { height: 79px; }
  .banner--tall { height: 105px; }
  .banner-art { position: absolute; left: 0; top: 0; width: 848px; height: 100%; display: block; }
  .texture { position: absolute; inset: 0; background: var(--texture-grey); }
  .txt { position: absolute; line-height: 1; white-space: nowrap; }

  .brand { font-weight: 800; letter-spacing: -2px; }
  .strap { font-weight: 700; font-size: 14px; }
  .tagline { font-weight: 500; font-size: 13.5px; letter-spacing: -0.3px; }
  .cta { font-weight: 800; }

  /* second set */
  .gazettor-mkt .brand { left: 52px; top: 4px; font-size: 31px; line-height: 33px; letter-spacing: -0.5px; }
  .gazettor-mkt .strap { left: 364px; top: 25px; font-size: 16.5px; font-weight: 600; letter-spacing: -0.3px; }
  .gazettor-mkt .tagline { left: 364px; top: 54px; font-size: 13.8px; font-weight: 600; }
  .gazettor-mkt .cta { left: 620px; width: 119px; top: 60px; text-align: center; color: var(--white); font-size: 17.5px; letter-spacing: -0.6px; }

  .gazettor-hr .brand { left: 29px; top: 4px; font-size: 40px; color: var(--purple); }
  .gazettor-hr .tagline { left: 29px; top: 51px; color: var(--purple); font-size: 14px; font-weight: 600; }
  .gazettor-hr .strap { left: 364px; top: 27px; font-size: 16.5px; font-weight: 600; color: var(--white); letter-spacing: -0.3px; }
  .gazettor-hr .cta { left: 620px; width: 119px; top: 60px; text-align: center; color: var(--purple); font-size: 17.5px; letter-spacing: -0.6px; }

  .wispo-mkt .brand { left: 28px; top: 6px; font-size: 40px; }
  .wispo-mkt .tagline { left: 29px; top: 48px; }
  .wispo-mkt .strap { right: 31px; top: 50px; font-size: 14.4px; }
  .wispo-mkt .cta { left: 722px; width: 94px; top: 18px; text-align: center; font-size: 10px; letter-spacing: 0.4px; }

  .wispo-hr .brand { left: 28px; top: 5px; font-size: 42px; color: var(--purple); }
  .wispo-hr .tagline { left: 29px; top: 45px; }
  .wispo-hr .strap { left: 284px; top: 42px; font-size: 14.3px; }
  .wispo-hr .cta { left: 722px; width: 94px; top: 34px; text-align: center; color: var(--white); font-size: 13.5px; letter-spacing: -0.6px; }

  /* first set */
  .badge-text { position: absolute; transform: translate(-50%, -50%); text-align: center; font-weight: 800; white-space: nowrap; }

  .wispo-hr-alt .brand { left: 44px; top: 22px; font-size: 23px; letter-spacing: 0; color: var(--white); }
  .wispo-hr-alt .strap { left: 44px; top: 58px; font-size: 14.9px; color: var(--white); }
  .wispo-hr-alt .cta { left: 342px; top: 24px; font-size: 14px; }
  .wispo-hr-alt .badge-text { left: 701px; top: 46px; font-size: 14.5px; line-height: 18px; color: var(--white); }

  .gazettor-hr-alt .brand { left: 123px; top: 18px; font-size: 25px; letter-spacing: 0; }
  .gazettor-hr-alt .strap { left: 123px; top: 61px; font-size: 14px; }
  .gazettor-hr-alt .cta { left: 471px; top: 32px; font-size: 18.6px; color: var(--sun); }
  .gazettor-hr-alt .badge-text { left: 721px; top: 49px; font-size: 17.4px; line-height: 21px; }

  .gazettor-mkt-alt .brand { left: 118px; top: 23px; font-size: 23px; letter-spacing: 0; }
  .gazettor-mkt-alt .strap { left: 118px; top: 65px; font-size: 14px; }
  .gazettor-mkt-alt .cta { left: 522px; top: 71px; font-size: 14px; color: var(--sun); }
  .gazettor-mkt-alt .badge-text { left: 721px; top: 49px; font-size: 17.4px; line-height: 21px; }
</style>
</head>
<body>
<main class="canvas">
  <div class="stage"></div>
  <h2 class="set-title set-title--second">Second Set of Banners</h2>

  <!-- Marketing Gazettor -->
  <section class="banner banner--slim gazettor-mkt" style="top:158px">
    <svg class="banner-art" viewBox="0 0 848 79" aria-hidden="true">
      <path d="M313 79 C316 28 350 0 400 0 H848 V40 C848 62 830 79 808 79 Z" fill="var(--ink)"/>
      <path d="M326 79 C330 30 362 0 410 0 H842 V36 C842 60 826 79 800 79 Z" fill="var(--gold)"/>
      <circle cx="798" cy="27" r="26" fill="var(--ink)"/>
      <circle cx="798" cy="27" r="7" fill="var(--gold)"/>
      <path d="M620 61 Q620 55 626 55 H733 Q739 55 739 61 V79 H620 Z" fill="var(--ink)"/>
    </svg>
    <div class="txt brand">MARKETING<br>GAZETTOR</div>
    <div class="txt strap">Essential Whitepapers for HR Professionals...</div>
    <div class="txt tagline">Your No.1 Whitepaper Resource</div>
    <div class="txt cta">click here</div>
  </section>

  <!-- HR Gazettor -->
  <section class="banner banner--slim gazettor-hr" style="top:289px">
    <svg class="banner-art" viewBox="0 0 848 79" aria-hidden="true">
      <path d="M313 79 C316 28 350 0 400 0 H848 V40 C848 62 830 79 808 79 Z" fill="var(--purple-soft)"/>
      <path d="M326 79 C330 30 362 0 410 0 H842 V36 C842 60 826 79 800 79 Z" fill="var(--purple)"/>
      <circle cx="798" cy="27" r="26" fill="var(--white)"/>
      <circle cx="798" cy="27" r="7" fill="var(--purple)"/>
      <path d="M620 61 Q620 55 626 55 H733 Q739 55 739 61 V79 H620 Z" fill="var(--white)"/>
    </svg>
    <div class="txt brand">HR GAZETTOR</div>
    <div class="txt tagline">Your No.1 Whitepaper Resource</div>
    <div class="txt strap">Essential Whitepapers for HR Professionals...</div>
    <div class="txt cta">click here</div>
  </section>

  <!-- Marketing Wispo -->
  <section class="banner banner--slim wispo-mkt" style="top:420px">
    <svg class="banner-art" viewBox="0 0 848 79" aria-hidden="true">
      <rect x="722" y="9" width="94" height="27" rx="3" fill="var(--gold)"/>
      <rect x="29" y="70" width="787" height="20" rx="6" fill="var(--gold)"/>
    </svg>
    <div class="txt brand">MARKETING WISPO</div>
    <div class="txt tagline">Your No.1 Whitepaper Resource</div>
    <div class="txt strap">Essential Whitepapers for Marketing Professionals...</div>
    <div class="txt cta">CLICK HERE</div>
  </section>

  <!-- HR Wispo -->
  <section class="banner banner--slim wispo-hr" style="top:551px">
    <svg class="banner-art" viewBox="0 0 848 79" aria-hidden="true">
      <rect x="722" y="26" width="94" height="30" rx="3" fill="var(--purple)"/>
      <rect x="29" y="70" width="787" height="20" rx="6" fill="var(--purple)"/>
    </svg>
    <div class="txt brand">HR WISPO</div>
    <div class="txt tagline">Your No.1 Whitepaper Resource</div>
    <div class="txt strap">Essential Whitepapers for HR Professionals...</div>
    <div class="txt cta">Click Here</div>
  </section>

  <h2 class="set-title set-title--first">First Set of Banners</h2>

  <!-- HR Wispo, alternate -->
  <section class="banner banner--tall wispo-hr-alt" style="top:768px">
    <div class="texture" role="img" aria-label="Speckled grey texture"></div>
    <svg class="banner-art" viewBox="0 0 848 105" aria-hidden="true">
      <defs>
        <linearGradient id="warm" x1="0" y1="0" x2="1" y2="1">
          <stop offset="0" stop-color="var(--orange-light)"/>
          <stop offset="1" stop-color="var(--orange)"/>
        </linearGradient>
      </defs>
      <rect x="0" y="93" width="459" height="24" rx="10" fill="var(--orange)"/>
      <path d="M0 0 H430 C460 0 481 22 481 48 C481 72 465 90 450 93 H0 Z" fill="var(--slate)"/>
      <path d="M640 0 H848 V105 H660 Z" fill="url(#warm)"/>
      <path d="M618 0 H700 V105 H645 L605 52 C594 34 600 8 618 0 Z" fill="var(--sun)" stroke="var(--ink)" stroke-width="2.5"/>
      <circle cx="700" cy="50" r="77" fill="var(--slate)"/>
      <circle cx="724" cy="108" r="34" fill="var(--orange)"/>
      <path d="M772 104 C800 66 796 28 778 10" fill="none" stroke="var(--ink)" stroke-width="1.6"/>
      <path d="M773 3 L786 12 L774 16 Z" fill="var(--ink)"/>
      <rect x="327" y="16" width="112" height="32" rx="16" fill="var(--sun)"/>
      <circle cx="433" cy="50" r="32" fill="var(--sun)"/>
      <circle cx="433" cy="50" r="14" fill="var(--ink)"/>
    </svg>
    <div class="txt brand">HR Wispo</div>
    <div class="txt strap">Essential Whitepapers for HR Professionals</div>
    <div class="txt cta">Click Me</div>
    <div class="badge-text">Your No.1<br>Whitepaper<br>Resource</div>
  </section>

  <!-- HR Gazettor, alternate -->
  <section class="banner banner--tall gazettor-hr-alt" style="top:894px">
    <div class="texture" role="img" aria-label="Speckled grey texture"></div>
    <svg class="banner-art" viewBox="0 0 848 105" aria-hidden="true">
      <rect x="57" y="0" width="700" height="105" rx="52" fill="var(--ink)"/>
      <rect x="66" y="3" width="650" height="95" rx="47" fill="var(--sun)"/>
      <circle cx="721" cy="52" r="88" fill="var(--ink)"/>
      <circle cx="721" cy="52" r="63" fill="var(--sun)"/>
      <rect x="452" y="24" width="140" height="36" rx="18" fill="var(--ink)"/>
      <circle cx="582" cy="42" r="29" fill="var(--ink)"/>
      <circle cx="582" cy="42" r="8" fill="var(--sun)"/>
    </svg>
    <div class="txt brand">HR Gazettor</div>
    <div class="txt strap">Essential Whitepapers for HR Professionals</div>
    <div class="txt cta">Click Me</div>
    <div class="badge-text">Your No.1<br>Whitepaper<br>Resource</div>
  </section>

  <!-- Marketing Gazettor, alternate -->
  <section class="banner banner--tall gazettor-mkt-alt" style="top:1020px">
    <div class="texture" role="img" aria-label="Speckled grey texture"></div>
    <svg class="banner-art" viewBox="0 0 848 105" aria-hidden="true">
      <polygon points="0,27 63,25 36,105 0,105" fill="var(--steel)"/>
      <polygon points="805,45 848,19 848,105 807,105" fill="var(--steel)"/>
      <rect x="77" y="0" width="740" height="105" rx="52" fill="var(--coral)"/>
      <circle cx="601" cy="51" r="99" fill="var(--coral-deep)"/>
      <circle cx="721" cy="50" r="77" fill="var(--ink)"/>
      <circle cx="721" cy="50" r="62" fill="var(--sun)"/>
      <rect x="517" y="64" width="104" height="28" rx="14" fill="var(--cocoa)"/>
      <circle cx="608" cy="78" r="20" fill="var(--cocoa)"/>
      <circle cx="608" cy="78" r="6" fill="var(--sun)"/>
    </svg>
    <div class="txt brand">Marketing Gazettor</div>
    <div class="txt strap">Essential Whitepapers for Marketing Professionals</div>
    <div class="txt cta">Click Me</div>
    <div class="badge-text">Your No.1<br>Whitepaper<br>Resource</div>
  </section>
</main>
</body>
</html>
```